Stationery including letterhead, business cards, for a new Chartered Accounting Practice

I need a new set of stationery including letterhead, business cards, for a new Chartered Accounting Practice based in Melbourne, Victoria, Australia called "Brody Kettleworth, Chartered Accountant".

I will be providing Auditing and general consulting advice to small and medium business enterprises. The final design should communicate trust, wisdom and security.

Target Market(s)

Target Market English speaking, Australians. Proprietors small and medium sized businesses - aged 45-65. Fellow professionals - lawyers, investment consultants, other accountants. Retirees - aged 60 and over

Industry/Entity Type

Accountant

Font styles to use
Serif

Colors
0355a3

Requirements
Must have
• The final design should convey trust, wisdom and security.
• Names of practice "Brody Kettleworth , Chartered Accountant"
• Contact details:
• Address 214 Carrowdale Street, Fennick Vale, Victoria, 3058, Australia
• Telephone: 047 000 3815
• Email: brodykettleworth@mailbarrow.net
Nice to have
• an expensive and professional design, the letterhead should be timeless with a logo on white space
Should not have
• no bright/fluro colours

```html
<!DOCTYPE html>
<html lang="en">
<head>
<meta charset="utf-8">
<title>Brody Kettleworth – Stationery Set</title>
<link href="https://fonts.googleapis.com/css2?family=Noto+Sans:wght@400;500&family=Arimo:wght@400&display=swap" rel="stylesheet">
<style>
  :root {
    --bg: #d3d3d5;
    --paper: #ffffff;
    --ink: #2a2a2a;
    --brand-grey: #6c6c6e;
    --folder: #2b2b2b;
    --folder-spine: #222222;
    --folder-text: #8d8d8f;
    --card-dark: #2e2e2e;
    --signature: #b9bfd6;
  }
  * { box-sizing: border-box; margin: 0; padding: 0; }
  html, body { width: 1200px; height: 991px; overflow: hidden; }
  body { background: var(--bg); position: relative; font-family: "Arimo", Arial, sans-serif; color: var(--ink); }

  .piece { position: absolute; background: var(--paper); }
  .brand-name { font-family: "Noto Sans", sans-serif; font-weight: 500; color: var(--brand-grey); letter-spacing: 0.2px; white-space: nowrap; }
  .brand-role { font-family: "Noto Sans", sans-serif; font-weight: 400; color: var(--brand-grey); white-space: nowrap; }
  .brand-square { position: absolute; background: var(--brand-grey); }

  /* Letterhead */
  .letterhead { left: 70px; top: 103px; width: 397px; height: 560px; }
  .letterhead .brand-square { left: 33px; top: 33px; width: 18px; height: 18px; }
  .letterhead .brand-name { position: absolute; left: 66px; top: 31px; font-size: 12.5px; }
  .letterhead .brand-role { position: absolute; left: 66px; top: 48px; font-size: 6.5px; }
  .letterhead .contact { position: absolute; right: 32px; top: 34px; font-size: 5px; line-height: 6.4px; text-align: right; }
  .letterhead .date { position: absolute; left: 33px; top: 150px; font-size: 5.6px; }
  .letterhead .recipient { position: absolute; left: 33px; top: 163px; font-size: 5.6px; line-height: 7px; }
  .letterhead .salutation { position: absolute; left: 33px; top: 238px; font-size: 5.6px; }
  .letterhead .body { position: absolute; left: 33px; top: 255px; width: 333px; font-size: 5.6px; line-height: 7px; text-align: justify; }
  .letterhead .body p { margin-bottom: 6px; }
  .letterhead .closing { position: absolute; left: 33px; top: 383px; font-size: 5.6px; line-height: 7px; }
  .letterhead .signature { position: absolute; left: 80px; top: 378px; width: 60px; height: 22px; background: var(--signature); opacity: 0.6; }

  /* Folder */
  .folder { left: 506px; top: 90px; width: 431px; height: 575px; background: var(--folder); border-radius: 4px; overflow: hidden; }
  .folder .spine { position: absolute; left: 0; top: 0; width: 26px; height: 100%; background: var(--folder-spine); }
  .folder .mark-square { position: absolute; left: 188px; top: 120px; width: 60px; height: 60px; background: var(--folder-text); }
  .folder .brand-name { position: absolute; left: 0; width: 100%; text-align: center; top: 487px; font-size: 21px; color: var(--folder-text); padding-left: 26px; }
  .folder .brand-role { position: absolute; left: 0; width: 100%; text-align: center; top: 513px; font-size: 9.5px; color: var(--folder-text); padding-left: 26px; }

  /* Business cards */
  .card-front { left: 66px; top: 696px; width: 170px; height: 94px; }
  .card-front .brand-square { left: 15px; top: 19px; width: 12px; height: 12px; }
  .card-front .brand-name { position: absolute; left: 35px; top: 17px; font-size: 8.2px; }
  .card-front .brand-role { position: absolute; left: 35px; top: 28px; font-size: 4.3px; }
  .card-front .contact { position: absolute; left: 15px; top: 74px; font-size: 3.6px; line-height: 4.6px; color: var(--brand-grey); }
  .card-back { left: 66px; top: 810px; width: 170px; height: 94px; background: var(--card-dark); display: flex; align-items: center; justify-content: center; }
  .card-back .brand-name { font-size: 8px; color: var(--folder-text); }

  /* Envelope front */
  .envelope-front { left: 266px; top: 696px; width: 415px; height: 208px; }
  .envelope-front .brand-square { left: 27px; top: 28px; width: 20px; height: 20px; }
  .envelope-front .brand-name { position: absolute; left: 60px; top: 25px; font-size: 12.5px; }
  .envelope-front .brand-role { position: absolute; left: 60px; top: 42px; font-size: 6.5px; }
  .envelope-front .address { position: absolute; left: 27px; top: 60px; font-size: 5.3px; line-height: 6.6px; }

  /* Envelope back */
  .envelope-back { left: 718px; top: 696px; width: 415px; height: 208px; }
  .envelope-back svg { position: absolute; left: 0; top: 0; }
  .envelope-back .brand-name { position: absolute; left: 0; width: 100%; text-align: center; top: 24px; font-size: 7px; color: var(--folder-text); }
</style>
</head>
<body>

  <section class="piece letterhead" aria-label="Letterhead">
    <span class="brand-square"></span>
    <div class="brand-name">BRODY KETTLEWORTH</div>
    <div class="brand-role">Chartered Accountant</div>
    <div class="contact">
      047 000 3815 / brodykettleworth@mailbarrow.net<br>
      214 Carrowdale Street, Fennick Vale<br>
      Victoria, 3058, Australia
    </div>
    <div class="date">30.09.2017</div>
    <div class="recipient">Recipient's name<br>Kastanienweg 7<br>10115 Berlin<br>Germany</div>
    <div class="salutation">Dear sir,</div>
    <div class="body">
      <p>Thank you for the opportunity to review the accounts of your business for the past financial year. We have completed our examination of the records provided and prepared a summary of the key findings. Overall, the books are well kept and the reporting is in line with current standards. A few minor items need attention before lodgement.</p>
      <p>Our review found that several expense claims lack supporting receipts, and two asset purchases were recorded in the wrong period. We recommend that these be corrected and that a simple monthly reconciliation routine is adopted. This will reduce the time needed at year end and give you a clearer view of cash flow throughout the year.</p>
      <p>We would be glad to meet and discuss these points in person. Please contact our office to arrange a suitable time, and bring any further documents you wish us to consider.</p>
      <p>Thank you again for your trust in our practice. We look forward to working with you in the year ahead.</p>
    </div>
    <div class="closing">Yours Sincerely,<br>Tessa Morrow</div>
    <div class="signature" role="img" aria-label="Handwritten signature"></div>
  </section>

  <section class="piece folder" aria-label="Presentation folder">
    <span class="spine"></span>
    <span class="mark-square"></span>
    <div class="brand-name">BRODY KETTLEWORTH</div>
    <div class="brand-role">Chartered Accountant</div>
  </section>

  <section class="piece card-front" aria-label="Business card front">
    <span class="brand-square"></span>
    <div class="brand-name">BRODY KETTLEWORTH</div>
    <div class="brand-role">Chartered Accountant</div>
    <div class="contact">
      047 000 3815 / brodykettleworth@mailbarrow.net<br>
      214 Carrowdale Street, Fennick Vale, Victoria, 3058, Australia
    </div>
  </section>

  <section class="piece card-back" aria-label="Business card back">
    <div class="brand-name">BRODY KETTLEWORTH</div>
  </section>

  <section class="piece envelope-front" aria-label="Envelope front">
    <span class="brand-square"></span>
    <div class="brand-name">BRODY KETTLEWORTH</div>
    <div class="brand-role">Chartered Accountant</div>
    <div class="address">214 Carrowdale Street, Fennick Vale<br>Victoria, 3058, Australia</div>
  </section>

  <section class="piece envelope-back" aria-label="Envelope back">
    <svg width="415" height="60" viewBox="0 0 415 60" aria-hidden="true">
      <path d="M0 0 H415 V14 L395 58 H20 L0 14 Z" fill="var(--folder)"/>
    </svg>
    <div class="brand-name">BRODY KETTLEWORTH</div>
  </section>

</body>
</html>
```